Food Choices & Validated Experience Outcomes in Quality Tracking

We have spent the past 7 years studying food choices and rate of PD progression. We want to show people which foods have the most significant impact. <br/><br/>The infographic attached called "Kindred Living in QT" is the first in this 6-part series, recently designed by someone on PixelGuild. I'd like this entire series to "pair nicely" with one another, but also have unique personality, which is why I've opened the contest up. <br/><br/>The VEX-QT scale is the point of reference, it explains that higher scores are worse, low scores are better. I'd like to stick with the green is good, red is bad theme. ish. <br/><br/>The blue bar chart with food is "the grand finale." THIS is the information people have been waiting for for decades! I expect this to be highly circulated-- passed to physicians, support groups, getting tens of thousands of shares online! Below, I uploaded the 2019 version (also produced by someone from Pixel Guild). On my ppt screen shot, that data on the bottom left is also REALLY important. Can make another bar chart? Or find some other creative way to communicate it? OK to not include the p-values (OK to remove the far right column). Thanks!

Target Market(s)

Patients, their partners/ families, and health care providers.

Requirements
Must have
• Must include the legend-- some version of the VEX-QT scale vs. Quality of Life, as a point of reference. If possible, I'd like to stick with [some shade of] green is good, with it being clear that scores are getting worse [red-ish] as the scores increase.
• Must have the website, so people can go look for more information/ details about the project.
Nice to have
• Coordination with the "Kindred Living ..." infographic below.

```html
<!DOCTYPE html>
<html lang="en">
<head>
<meta charset="utf-8">
<title>Food Choices &amp; Parkinson's Disease Progression</title>
<link rel="stylesheet" href="https://fonts.googleapis.com/css2?family=Source+Serif+4:ital,wght@0,400;0,700&family=Source+Sans+3:ital,wght@0,400;0,600;0,700;1,400;1,600;1,700&display=swap">
<style>
  :root {
    --card: #f3f3f3;
    --panel: #efefef;
    --panel-line: #dcdcdc;
    --red: #c0132b;
    --red-deep: #a30f24;
    --ink: #1a1a1a;
    --black: #0d0d0d;
    --poor: #b8182b;
    --fair: #ea7a58;
    --good: #c3d97e;
    --excellent: #7bbf47;
    --axis-strip: #d9d9d9;
    --green-dark: #1f7a3a;
    --green-mid: #4b9a3a;
    --green-light: #8dc63f;
    --bad-bright: #e02232;
    --bad-dark: #8e1a2a;
    --serif: "Source Serif 4", Georgia, serif;
    --sans: "Source Sans 3", "Helvetica Neue", Arial, sans-serif;
  }
  * { margin: 0; padding: 0; box-sizing: border-box; }
  html, body { width: 1200px; height: 1026px; overflow: hidden; }
  body { background: var(--card); font-family: var(--sans); color: var(--ink); position: relative; }

  .panel { position: absolute; }
  .panel svg { display: block; width: 100%; height: 100%; }

  /* Title block */
  .title-block { left: 28px; top: 30px; width: 559px; height: 468px; }
  .title-block .backdrop { position: absolute; inset: 0; }
  .title-block .content { position: absolute; left: 32px; top: 57px; right: 16px; color: #fff; }
  .title-block h1 { font-family: var(--serif); font-weight: 700; font-size: 46px; line-height: 51px; letter-spacing: -0.2px; }
  .title-block .authors { font-style: italic; font-size: 22px; margin-top: 14px; }
  .title-block .dots { font-size: 22px; font-weight: 700; letter-spacing: 2px; margin-top: 10px; line-height: 22px; }
  .title-block .label { font-style: italic; font-size: 22px; margin-top: 20px; line-height: 26px; }
  .title-block .url { font-family: var(--serif); font-size: 22px; line-height: 26px; }
  .title-block .year { position: absolute; right: 10px; top: 8px; font-family: var(--serif); font-weight: 700; font-size: 38px; color: var(--red); }

  .chart-panel { background: var(--panel); border: 1px solid var(--panel-line); }
  .qol-chart { left: 610px; top: 27px; width: 564px; height: 472px; }
  .behavior-chart { left: 28px; top: 522px; width: 560px; height: 477px; }
  .servings-chart { left: 612px; top: 522px; width: 562px; height: 477px; }

  .chart-title { font-family: var(--serif); font-weight: 700; font-size: 19px; fill: var(--ink); }
  .tick { font-family: var(--sans); font-weight: 700; font-size: 15px; fill: var(--ink); }
  .band-label { font-family: var(--sans); font-weight: 600; font-size: 21px; fill: #fff; }
  .side-label { font-family: var(--sans); font-weight: 700; font-style: italic; font-size: 18px; fill: #fff; }
  .axis-caption { font-family: var(--sans); font-style: italic; font-weight: 600; font-size: 15px; fill: var(--ink); }
  .row-label { font-family: var(--sans); font-size: 12.5px; fill: var(--ink); }
  .pill-value { font-family: var(--sans); font-weight: 600; font-size: 12px; fill: #fff; }
  .footnote { font-family: var(--sans); font-size: 13px; fill: var(--ink); }
  .food-label { font-family: var(--sans); font-size: 11.5px; fill: var(--ink); }
  .legend-pill { font-family: var(--sans); font-size: 9px; fill: #fff; }
  .scale-name { font-family: var(--sans); font-weight: 700; font-style: italic; font-size: 14px; fill: var(--ink); }
  .scale-expansion { font-family: var(--sans); font-style: italic; font-weight: 600; font-size: 14px; fill: var(--ink); }
</style>
</head>
<body>

<section class="panel title-block">
  <svg class="backdrop" viewBox="0 0 559 468" preserveAspectRatio="none" aria-hidden="true">
    <defs>
      <linearGradient id="titleRed" x1="0" y1="0" x2="0" y2="1">
        <stop offset="0" stop-color="#c8142e"/>
        <stop offset="1" stop-color="#a80f25"/>
      </linearGradient>
    </defs>
    <rect x="0" y="0" width="559" height="468" fill="url(#titleRed)"/>
    <path d="M0 0 H559 V54 H478 C462 54 454 40 448 28 C442 18 436 14 426 14 H0 Z" fill="#e4e4e4"/>
  </svg>
  <div class="year">2020</div>
  <div class="content">
    <h1>Food Choices &amp;<br>Parkinson’s Disease<br>Progression</h1>
    <p class="authors">RT Halvorsen et al.</p>
    <p class="dots">•••</p>
    <p class="label">For study details:</p>
    <p class="url">www.LivingWellWithVexQT.org</p>
    <p class="label">To participate in this study:</p>
    <p class="url">www.CareStudyQT.Northvale.edu</p>
  </div>
</section>

<section class="panel qol-chart">
  <svg viewBox="610 27 564 472" aria-label="Line chart: VEX-QT score rises with years since diagnosis, moving from Good toward Poor quality of life">
    <text class="chart-title" x="923" y="42" text-anchor="middle">Correlation Between Quality of Life and</text>
    <text class="chart-title" x="923" y="67" text-anchor="middle">VEX-QT Score</text>

    <rect x="610" y="87" width="33" height="356" fill="var(--black)"/>
    <text class="side-label" transform="translate(633 265) rotate(-90)" text-anchor="middle">VEX-QT SCORE</text>

    <rect x="691" y="87" width="445" height="166" fill="var(--poor)"/>
    <rect x="691" y="253" width="445" height="63" fill="var(--fair)"/>
    <rect x="691" y="316" width="445" height="62" fill="var(--good)"/>
    <rect x="691" y="378" width="445" height="65" fill="var(--excellent)"/>

    <text class="tick" x="687" y="92" text-anchor="end">2500</text>
    <text class="tick" x="687" y="175" text-anchor="end">2000</text>
    <text class="tick" x="687" y="253" text-anchor="end">1500</text>
    <text class="tick" x="687" y="317" text-anchor="end">1000</text>
    <text class="tick" x="687" y="384" text-anchor="end">500</text>

    <text class="band-label" x="1112" y="170" text-anchor="end">Poor</text>
    <text class="band-label" x="1114" y="294" text-anchor="end">Fair</text>
    <text class="band-label" x="1114" y="356" text-anchor="end">Good</text>
    <text class="band-label" x="1114" y="418" text-anchor="end">Excellent</text>

    <line x1="697" y1="378" x2="1063" y2="225" stroke="#fff" stroke-width="2.5"/>
    <g fill="#fff">
      <circle cx="739" cy="361" r="6"/>
      <circle cx="792" cy="338" r="6"/>
      <circle cx="857" cy="313" r="6"/>
      <circle cx="915" cy="288" r="6"/>
      <circle cx="981" cy="261" r="6"/>
      <circle cx="1044" cy="234" r="6"/>
    </g>

    <rect x="1142" y="87" width="31" height="356" fill="var(--black)"/>
    <text class="side-label" transform="translate(1163 265) rotate(-90)" text-anchor="middle">Quality Of Life</text>

    <rect x="610" y="450" width="564" height="48" fill="var(--axis-strip)"/>
    <g class="tick" text-anchor="middle">
      <text x="679" y="470">0</text>
      <text x="739" y="470">5</text>
      <text x="797" y="470">10</text>
      <text x="859" y="470">15</text>
      <text x="922" y="470">20</text>
      <text x="984" y="470">25</text>
      <text x="1046" y="470">30</text>
      <text x="1108" y="470">35</text>
    </g>
    <g stroke="var(--ink)" stroke-width="1.5" fill="var(--ink)">
      <line x1="654" y1="485" x2="830" y2="485"/>
      <line x1="970" y1="485" x2="1131" y2="485"/>
      <path d="M651 485 l9 -4 v8 z" stroke="none"/>
      <path d="M1135 485 l-9 -4 v8 z" stroke="none"/>
    </g>
    <text class="axis-caption" x="900" y="490" text-anchor="middle">Years Since Diagnosis</text>
  </svg>
</section>

<section class="panel chart-panel behavior-chart">
  <svg viewBox="28 522 560 477" aria-label="Bar chart: estimated impact of dietary behaviours on VEX-QT score">
    <text class="chart-title" x="303" y="563" text-anchor="middle">Impact of Dietary Behaviors on PD Progression</text>

    <text class="axis-caption" transform="translate(72 770) rotate(-90)" text-anchor="middle" style="font-size:14px">Estimated Impact on VEX-QT</text>
    <rect x="86" y="594" width="31" height="349" rx="15.5" fill="var(--black)"/>

    <g class="pill-value" text-anchor="middle">
      <text x="101" y="619">-146</text>
      <text x="101" y="664">-121</text>
      <text x="101" y="708">-106</text>
      <text x="101" y="753">-105</text>
      <text x="101" y="797">-86</text>
      <text x="101" y="842">-71</text>
      <text x="101" y="887">366</text>
      <text x="101" y="931">389</text>
    </g>

    <g class="row-label">
      <text x="121" y="609">I cook most of my meals</text>
      <text x="121" y="654">I avoid artificial sweetners</text>
      <text x="121" y="698">I avoid artificial colors, flavors</text>
      <text x="121" y="743">I routinely prepare meals for others</text>
      <text x="121" y="787">I try to eat organically grown foods when possible</text>
      <text x="121" y="832">I buy from local farmers</text>
      <text x="121" y="877">I find it difficult to afford healthy food</text>
      <text x="121" y="921">It is difficult to afford groceries</text>
    </g>

    <g>
      <rect x="121" y="612" width="185" height="2.6" fill="var(--green-dark)"/><rect x="121" y="616" width="185" height="2.6" fill="var(--green-dark)"/>
      <rect x="121" y="657" width="152" height="2.6" fill="var(--green-dark)"/><rect x="121" y="661" width="152" height="2.6" fill="var(--green-dark)"/>
      <rect x="121" y="701" width="129" height="2.6" fill="#2f8a3c"/><rect x="121" y="705" width="129" height="2.6" fill="#2f8a3c"/>
      <rect x="121" y="746" width="129" height="2.6" fill="#3c923b"/><rect x="121" y="750" width="129" height="2.6" fill="#3c923b"/>
      <rect x="121" y="790" width="92" height="2.6" fill="#6aae42"/><rect x="121" y="794" width="92" height="2.6" fill="#6aae42"/>
      <rect x="121" y="835" width="59" height="2.6" fill="var(--green-light)"/><rect x="121" y="839" width="59" height="2.6" fill="var(--green-light)"/>
      <rect x="121" y="880" width="360" height="2.6" fill="var(--bad-bright)"/><rect x="121" y="884" width="360" height="2.6" fill="var(--bad-bright)"/>
      <rect x="121" y="924" width="401" height="2.6" fill="#b01a2c"/><rect x="121" y="928" width="401" height="2.6" fill="#b01a2c"/>
    </g>

    <text class="footnote" x="307" y="966" text-anchor="middle">N = 1503-1521 (per question, if answered).</text>
    <text class="footnote" x="307" y="986" text-anchor="middle">All regression analyses adjusted for age, gender, income, and years since diagnosis.</text>
  </svg>
</section>

<section class="panel chart-panel servings-chart">
  <svg viewBox="612 522 562 477" aria-label="Bar chart: impact of 2 to 4 servings per week of each food on VEX-QT symptom severity">
    <text class="chart-title" x="893" y="565" text-anchor="middle">Impact of 2-4 Servings Per Week on</text>
    <text class="chart-title" x="893" y="590" text-anchor="middle">Symptom Severity</text>

    <g>
      <rect x="668" y="646" width="8" height="258" fill="#1c6e35"/>
      <rect x="688" y="735" width="8" height="169" fill="#1f7a3a"/>
      <rect x="708" y="751" width="8" height="153" fill="#25803a"/>
      <rect x="728" y="760" width="8" height="144" fill="#2f883a"/>
      <rect x="748" y="776" width="8" height="128" fill="#3d913a"/>
      <rect x="769" y="779" width="8" height="125" fill="#4b9a3a"/>
      <rect x="789" y="826" width="8" height="78" fill="#6caf3e"/>
      <rect x="809" y="853" width="8" height="51" fill="var(--green-light)"/>
      <rect x="829" y="878" width="8" height="26" fill="var(--bad-bright)"/>
      <rect x="849" y="865" width="8" height="39" fill="#dc2131"/>
      <rect x="870" y="860" width="8" height="44" fill="#d82030"/>
      <rect x="890" y="848" width="8" height="56" fill="#d21f30"/>
      <rect x="910" y="844" width="8" height="60" fill="#cc1e2f"/>
      <rect x="930" y="841" width="8" height="63" fill="#c71d2f"/>
      <rect x="950" y="836" width="8" height="68" fill="#c21d2e"/>
      <rect x="971" y="820" width="8" height="84" fill="#bb1c2e"/>
      <rect x="991" y="811" width="8" height="93" fill="#b41b2d"/>
      <rect x="1011" y="784" width="8" height="120" fill="#ad1b2d"/>
      <rect x="1031" y="774" width="8" height="130" fill="#a61b2c"/>
      <rect x="1051" y="766" width="8" height="138" fill="#9f1a2c"/>
      <rect x="1072" y="757" width="8" height="147" fill="#981a2b"/>
      <rect x="1092" y="749" width="8" height="155" fill="#921a2b"/>
      <rect x="1112" y="716" width="8" height="188" fill="var(--bad-dark)"/>
    </g>

    <g class="food-label" text-anchor="start">
      <text transform="translate(676 642) rotate(-90)">Fresh Vegetables</text>
      <text transform="translate(696 731) rotate(-90)">Fresh Fruit</text>
      <text transform="translate(716 747) rotate(-90)">Nuts/Seed</text>
      <text transform="translate(736 756) rotate(-90)">Fish</text>
      <text transform="translate(756 772) rotate(-90)">Wine</text>
      <text transform="translate(777 775) rotate(-90)">Olive Oil</text>
      <text transform="translate(797 822) rotate(-90)">Coconut Oil</text>
      <text transform="translate(817 849) rotate(-90)">Fresh Herbs</text>
      <text transform="translate(837 874) rotate(-90)">Milk</text>
      <text transform="translate(857 861) rotate(-90)">Cheese</text>
      <text transform="translate(878 856) rotate(-90)">Yogurt</text>
      <text transform="translate(898 844) rotate(-90)">Frozen Vegetables</text>
      <text transform="translate(918 840) rotate(-90)">Pork</text>
      <text transform="translate(938 837) rotate(-90)">Chicken</text>
      <text transform="translate(958 832) rotate(-90)">Plastic-Bottled Drinks</text>
      <text transform="translate(979 816) rotate(-90)">Soda</text>
      <text transform="translate(999 807) rotate(-90)">Pasta</text>
      <text transform="translate(1019 780) rotate(-90)">Beef</text>
      <text transform="translate(1039 770) rotate(-90)">Canned Vegetables</text>
      <text transform="translate(1059 762) rotate(-90)">Ice Cream</text>
      <text transform="translate(1080 753) rotate(-90)">Fried Foods</text>
      <text transform="translate(1100 745) rotate(-90)">Diet Soda</text>
      <text transform="translate(1120 712) rotate(-90)">Canned Fruit</text>
    </g>

    <rect x="651" y="909" width="483" height="26" rx="13" fill="var(--black)"/>
    <g class="pill-value" text-anchor="middle" style="font-size:11px">
      <text transform="translate(676 922) rotate(-60)">-225</text>
      <text transform="translate(696 922) rotate(-60)">-188</text>
      <text transform="translate(716 922) rotate(-60)">-161</text>
      <text transform="translate(736 922) rotate(-60)">-144</text>
      <text transform="translate(756 922) rotate(-60)">-115</text>
      <text transform="translate(777 922) rotate(-60)">-114</text>
      <text transform="translate(797 922) rotate(-60)">-79</text>
      <text transform="translate(817 922) rotate(-60)">-58</text>
      <text transform="translate(837 922) rotate(-60)">42</text>
      <text transform="translate(857 922) rotate(-60)">51</text>
      <text transform="translate(878 922) rotate(-60)">56</text>
      <text transform="translate(898 922) rotate(-60)">63</text>
      <text transform="translate(918 922) rotate(-60)">67</text>
      <text transform="translate(938 922) rotate(-60)">68</text>
      <text transform="translate(958 922) rotate(-60)">69</text>
      <text transform="translate(979 922) rotate(-60)">84</text>
      <text transform="translate(999 922) rotate(-60)">85</text>
      <text transform="translate(1019 922) rotate(-60)">106</text>
      <text transform="translate(1039 922) rotate(-60)">110</text>
      <text transform="translate(1059 922) rotate(-60)">120</text>
      <text transform="translate(1080 922) rotate(-60)">144</text>
      <text transform="translate(1100 922) rotate(-60)">146</text>
      <text transform="translate(1120 922) rotate(-60)">191</text>
    </g>

    <g>
      <line x1="657" y1="944" x2="818" y2="944" stroke="var(--green-light)" stroke-width="1.2"/>
      <path d="M653 944 l6 -3 v6 z" fill="var(--green-light)"/>
      <path d="M822 944 l-6 -3 v6 z" fill="var(--green-light)"/>
      <rect x="691" y="938" width="94" height="12" rx="6" fill="var(--green-light)"/>
      <text class="legend-pill" x="738" y="947" text-anchor="middle">Better Than Average</text>

      <line x1="831" y1="944" x2="1128" y2="944" stroke="var(--bad-bright)" stroke-width="1.2"/>
      <path d="M827 944 l6 -3 v6 z" fill="var(--bad-bright)"/>
      <path d="M1132 944 l-6 -3 v6 z" fill="var(--bad-bright)"/>
      <rect x="933" y="938" width="94" height="12" rx="6" fill="var(--bad-bright)"/>
      <text class="legend-pill" x="980" y="947" text-anchor="middle">Worse Than Average</text>
    </g>

    <text class="scale-name" x="893" y="967" text-anchor="middle">VEX-QT</text>
    <text class="scale-expansion" x="893" y="984" text-anchor="middle">Validated Experience Outcomes in Quality Tracking</text>
  </svg>
</section>

</body>
</html>
```